Consulting company needs Business Cards - rough concept provided

I'm looking for someone to take our business card idea and make is slick and polished - to communicate our high-end, sophisticated, serious consulting business. We have a rough layout we did in-house. We are open to ideas on repo-ing elements, adjusting sizes, typefaces etc... within the general concept we've already come up with. We want it to be super-clean and sophisticated. We want to keep the white backgrounds, and blue brand colors. Our goal is to print with painted blue edges on thick cardstock. Thank you!!

```html
<!DOCTYPE html>
<html lang="en">
<head>
<meta charset="utf-8">
<title>Northvale Business Card</title>
<link rel="stylesheet" href="https://fonts.googleapis.com/css2?family=Open+Sans:wght@700&family=Raleway:wght@200;300&family=Lato:wght@400;700&display=swap">
<style>
  :root {
    --bg: #2a2a2a;
    --card: #ffffff;
    --blue: #0a8fd8;
    --ink: #111111;
    --muted: #4a4a4a;
  }
  * { box-sizing: border-box; margin: 0; padding: 0; }
  html, body {
    width: 1200px; height: 875px; overflow: hidden;
    background: var(--bg);
  }
  .sheet {
    width: 1200px; height: 875px;
    display: flex; align-items: center; justify-content: center; gap: 40px;
  }
  .card {
    width: 540px; height: 310px;
    background: var(--card);
    border-radius: 28px;
    position: relative;
    overflow: hidden;
    box-shadow: 0 18px 40px rgba(0,0,0,.45);
  }

  /* Back: positioning statement */
  .statement {
    position: absolute; left: 42px; right: 28px; top: 50%;
    transform: translateY(-50%);
    font-size: 24px; line-height: 1.45;
    color: var(--ink);
  }
  .statement .row { display: block; white-space: nowrap; }
  .statement .row-indent { padding-left: 26px; }
  .statement .strong {
    font-family: "Open Sans", sans-serif; font-weight: 700;
    color: var(--ink);
  }
  .statement .fill {
    font-family: "Raleway", sans-serif; font-weight: 300;
    color: var(--blue);
  }

  /* Front: identity and contact */
  .brand-name {
    position: absolute; left: 40px; top: 50%;
    transform: translateY(-50%);
    font-family: "Open Sans", sans-serif; font-weight: 700;
    font-size: 34px; letter-spacing: 1px;
    color: var(--blue);
  }
  .divider {
    position: absolute; left: 300px; top: 60px; bottom: 60px;
    width: 1.5px; background: var(--blue);
  }
  .contact {
    position: absolute; left: 322px; top: 64px;
    font-family: "Lato", sans-serif; color: var(--muted);
    font-size: 13px; line-height: 1.45;
  }
  .contact .person {
    font-weight: 700; font-size: 21px; color: var(--blue); line-height: 1.1;
  }
  .contact .role { font-size: 14px; color: var(--ink); margin-bottom: 16px; }
  .contact .address { margin-bottom: 14px; }
  .contact .line { display: flex; align-items: center; gap: 8px; }
  .contact .line svg { width: 14px; height: 14px; flex: none; }
</style>
</head>
<body>
<main class="sheet">
  <section class="card card-back">
    <p class="statement">
      <span class="row"><span class="strong">We help</span> <span class="fill">[target demogrphic]</span> <span class="strong">achieve</span></span>
      <span class="row row-indent"><span class="fill">[desired emotional outcome]</span> <span class="strong">By</span></span>
      <span class="row"><span class="fill">Unique approach]</span> <span class="strong">because</span><span class="fill">[Our Brand</span></span>
      <span class="row row-indent"><span class="fill">beliefs]</span></span>
    </p>
  </section>

  <section class="card card-front">
    <div class="brand-name">NORTHVALE</div>
    <div class="divider"></div>
    <div class="contact">
      <div class="person">Dana Whitlow</div>
      <div class="role">Brand Consultant</div>
      <div class="address">4820 Harbor Lane, Ste 210<br>Lakemont, CA 90817</div>
      <div class="line">
        <svg viewBox="0 0 24 24" aria-hidden="true"><path fill="var(--blue)" d="M6.6 10.8a15.1 15.1 0 0 0 6.6 6.6l2.2-2.2a1 1 0 0 1 1-.25 11.4 11.4 0 0 0 3.6.57 1 1 0 0 1 1 1V20a1 1 0 0 1-1 1A17 17 0 0 1 3 4a1 1 0 0 1 1-1h3.5a1 1 0 0 1 1 1c0 1.25.2 2.450.57 3.57a1 1 0 0 1-.25 1z"/></svg>
        <span>(555) 014 2290</span>
      </div>
      <div class="line">
        <svg viewBox="0 0 24 24" aria-hidden="true"><path fill="var(--blue)" d="M2 6h20v12H2z"/><path fill="none" stroke="#fff" stroke-width="1.6" d="M2 6l10 7 10-7"/></svg>
        <span>dana@northvale.com</span>
      </div>
    </div>
  </section>
</main>
</body>
</html>
```